Veltrona Services

Double sided business cards with color on front and black and white on back. I have basic ideas and graphics, but am looking for someone to take them to the next level

```html
<!DOCTYPE html>
<html lang="en">
<head>
<meta charset="utf-8">
<title>Veltrona Services – Business Card</title>
<link href="https://fonts.googleapis.com/css2?family=Michroma&display=swap" rel="stylesheet">
<style>
  :root {
    --stage: #2b2b2b;
    --ink: #000000;
    --paper: #ffffff;
  }
  html, body {
    margin: 0;
    padding: 0;
    width: 1200px;
    height: 1015px;
    overflow: hidden;
    background: var(--stage);
  }
  .canvas {
    width: 1200px;
    height: 1015px;
    display: flex;
    flex-direction: column;
    align-items: center;
    justify-content: center;
    gap: 30px;
  }
  .card {
    width: 820px;
    height: 469px;
    display: block;
    box-shadow: 0 10px 30px rgba(0,0,0,0.5);
  }
  .card text {
    font-family: "Michroma", "Arial Black", sans-serif;
    font-weight: 400;
  }
  .on-dark { fill: var(--paper); }
  .on-light { fill: var(--ink); }
  .fill-ink { fill: var(--ink); }
  .fill-paper { fill: var(--paper); }
</style>
</head>
<body>
<main class="canvas">

  <!-- Back side: black and white -->
  <svg class="card card-back" viewBox="0 0 820 469" xmlns="http://www.w3.org/2000/svg">
    <rect class="fill-ink" x="0" y="0" width="820" height="469"/>
    <rect class="band fill-paper" x="0" y="200" width="330" height="80"/>
    <rect class="band fill-paper" x="490" y="110" width="330" height="80"/>
    <circle class="emblem-outer fill-ink" cx="410" cy="195" r="112"/>
    <circle class="emblem-ring fill-paper" cx="410" cy="195" r="92"/>
    <circle class="emblem-core fill-ink" cx="410" cy="195" r="78"/>
    <text class="brand-mark on-dark" x="410" y="201" font-size="15" text-anchor="middle" letter-spacing="1">VELTRONA</text>
    <text class="tagline on-dark" x="410" y="375" font-size="25" text-anchor="middle" letter-spacing="1">A CURATED EXPERIENCE ALL</text>
    <text class="tagline on-dark" x="410" y="415" font-size="25" text-anchor="middle" letter-spacing="1">THAT IS PROMISED IS CLARITY</text>
  </svg>

  <!-- Front side -->
  <svg class="card card-front" viewBox="0 0 820 469" xmlns="http://www.w3.org/2000/svg">
    <rect class="fill-paper" x="0" y="0" width="820" height="469"/>
    <rect class="band fill-ink" x="0" y="210" width="330" height="80"/>
    <rect class="band fill-ink" x="490" y="120" width="330" height="80"/>
    <circle class="emblem fill-paper" cx="410" cy="190" r="108"/>
    <text class="brand-mark on-light" x="410" y="196" font-size="16" text-anchor="middle" letter-spacing="1">VELTRONA</text>
    <text class="company-name on-light" x="455" y="345" font-size="28" text-anchor="middle" letter-spacing="1">VELTRONA SERVICES</text>
    <text class="phone on-light" x="455" y="403" font-size="46" text-anchor="middle">949-555-0147</text>
    <text class="email on-light" x="455" y="443" font-size="24" text-anchor="middle">info@veltrona.com</text>
  </svg>

</main>
</body>
</html>
```